Harborline Security and Surveillance Business Card

Business Card Design - Company Name:Freedom Security and SurveillanceWe are a Security Systems Integrator Specializing in Security Systems/ Video Surveillance and Access Control. Our areas of expertise are:Security SystemsVideo SurveillanceAccess ControlFire Alarm SystemsNetwork CablingCellular BoostersMy input is the Front of the Card is: logo, name of Business, My Name, Phone Number, and email.Rear of Card is the 6 areas of expertise, I just dont want the front to be very busy.
Name: Tom Werner
Title: President
Email: tom@harborlinesecsys.example
website: harborlinesecsys.example

```html
<!DOCTYPE html>
<html lang="en">
<head>
<meta charset="utf-8">
<title>Harborline Security and Surveillance – Business Card</title>
<link rel="stylesheet" href="https://fonts.googleapis.com/css2?family=Titillium+Web:wght@400;600&display=swap">
<style>
  :root {
    --page-bg: #eceef0;
    --card-bg: #161616;
    --card-bg-back: #1b1b1c;
    --brand-blue: #2a64c2;
    --text-light: #f2f2f2;
    --rule-grey: #8a8a8a;
  }
  * { box-sizing: border-box; margin: 0; padding: 0; }
  html, body {
    width: 1200px; height: 900px; overflow: hidden;
    background: var(--page-bg);
    font-family: "Titillium Web", Arial, sans-serif;
  }
  .canvas { position: relative; width: 1200px; height: 900px; }
  .card {
    position: absolute; top: 296px;
    width: 540px; height: 308px;
    border-radius: 3px;
    box-shadow: 0 6px 18px rgba(0,0,0,.18);
  }
  /* Back: areas of expertise */
  .card--back { left: 40px; background: var(--card-bg-back); }
  .back__brand {
    position: absolute; left: 0; right: 0; top: 78px;
    text-align: center;
  }
  .brand-mark {
    display: inline-block; width: 26px; height: 26px;
    border-radius: 50%; background: var(--brand-blue);
    vertical-align: middle; margin-right: 10px;
  }
  .back__name {
    display: inline-block; vertical-align: middle;
    color: var(--brand-blue); font-weight: 600;
    font-size: 25px; letter-spacing: 1.5px; text-transform: uppercase;
    line-height: 1.1; text-align: left;
  }
  .back__rule {
    position: absolute; left: 110px; right: 110px; top: 160px;
    height: 1px; background: var(--rule-grey);
  }
  .services {
    position: absolute; left: 0; right: 0; top: 176px;
    list-style: none; text-align: center;
    color: var(--text-light); font-size: 16px; line-height: 27px;
  }
  .services li { display: inline; }
  .services li + li::before {
    content: ""; display: inline-block; width: 5px; height: 5px;
    background: var(--text-light); margin: 0 9px; vertical-align: middle;
  }
  .services li.row-start::before { display: none; }
  .services li.row-start { display: inline; }
  .services .row-break { display: block; height: 0; }

  /* Front: contact */
  .card--front { left: 620px; background: var(--card-bg); }
  .front__brand {
    position: absolute; left: 28px; top: 34px;
    display: flex; align-items: center; gap: 8px;
  }
  .front__brand .brand-mark { width: 20px; height: 20px; margin: 0; }
  .front__name {
    color: var(--brand-blue); font-weight: 600; font-size: 15px;
    letter-spacing: 1px; text-transform: uppercase; line-height: 1;
  }
  .person {
    position: absolute; right: 34px; top: 100px; text-align: right;
  }
  .person__name {
    color: var(--brand-blue); font-weight: 600; font-size: 19px;
    letter-spacing: .5px; text-transform: uppercase; line-height: 1.1;
  }
  .person__title { color: var(--text-light); font-size: 15px; }
  .front__rule {
    position: absolute; left: 28px; right: 34px; top: 184px;
    height: 1.5px; background: var(--brand-blue);
  }
  .contacts {
    position: absolute; left: 30px; top: 204px; list-style: none;
    color: var(--text-light); font-size: 15.5px; line-height: 26px;
  }
  .contacts li { display: flex; align-items: center; gap: 10px; }
  .contacts svg { width: 16px; height: 16px; fill: var(--brand-blue); }
</style>
</head>
<body>
<main class="canvas">
  <section class="card card--back" aria-label="Card back">
    <div class="back__brand">
      <span class="brand-mark" aria-hidden="true"></span>
      <span class="back__name">Harborline Security<br>and Surveillance</span>
    </div>
    <div class="back__rule"></div>
    <ul class="services">
      <li class="row-start">Security Systems</li><li>Video Surveillance</li><li>Access Control</li>
      <span class="row-break"></span>
      <li class="row-start">Fire Alarm Systems</li><li>Network Cabling</li><li>Cellular Boosters</li>
    </ul>
  </section>

  <section class="card card--front" aria-label="Card front">
    <div class="front__brand">
      <span class="brand-mark" aria-hidden="true"></span>
      <span class="front__name">Harborline Security and Surveillance</span>
    </div>
    <div class="person">
      <p class="person__name">Tom Werner</p>
      <p class="person__title">President</p>
    </div>
    <div class="front__rule"></div>
    <ul class="contacts">
      <li>
        <svg viewBox="0 0 24 24" aria-hidden="true"><path d="M6.6 10.8a15.1 15.1 0 0 0 6.6 6.6l2.2-2.2c.3-.3.7-.4 1-.2 1.1.4 2.3.6 3.6.6.6 0 1 .4 1 1V20c0 .6-.4 1-1 1A17 17 0 0 1 3 4c0-.6.4-1 1-1h3.5c.6 0 1 .4 1 1 0 1.3.2 2.5.6 3.6.1.3 0 .7-.2 1z"/></svg>
        <span>123 456 7890</span>
      </li>
      <li>
        <svg viewBox="0 0 24 24" aria-hidden="true"><path d="M2 5h20v14H2z M3.5 6.5 12 13l8.5-6.5" fill="none" stroke="#2a64c2" stroke-width="0"/><path d="M2 5h20v14H2V5zm2 1.8V17h16V6.8l-8 6.1-8-6.1zM5.3 6 12 11.1 18.7 6H5.3z"/></svg>
        <span>tom@harborlinesecsys.example</span>
      </li>
      <li>
        <svg viewBox="0 0 24 24" aria-hidden="true"><path d="M12 2a10 10 0 1 0 0 20 10 10 0 0 0 0-20zm0 2c1.2 0 2.5 2.2 2.9 5H9.1C9.5 6.2 10.8 4 12 4zM4.3 11h2.8c0 .7 0 1.3.1 2H4.3a8 8 0 0 1 0-2zm4.8 0h5.8a17 17 0 0 1 0 2H9.1a17 17 0 0 1 0-2zm7.8 0h2.8a8 8 0 0 1 0 2h-2.8c.1-.7.1-1.3 0-2zM12 20c-1.2 0-2.5-2.2-2.9-5h5.8c-.4 2.8-1.7 5-2.9 5z"/></svg>
        <span>www.harborlinesecsys.example</span>
      </li>
    </ul>
  </section>
</main>
</body>
</html>
```